Business card design needed

Design:
Want the logo/design to have an enviromental feel
Simple look not to busy

Company Info:
Pre purchase building and pest inspections
Registered building practitoner DB-U 58147 (please include building commission logo in design)

Industry/Entity Type

Building

Contact Information for Business Card

Company name:
Fernvale Building and Pest inspections

Inspectors:
Dean Harker 0451 278 914
Greg Sutcliffe 0419 562 843
Email: fernvalebpi@mailpost.example

```html
<!DOCTYPE html>
<html lang="en">
<head>
<meta charset="utf-8">
<title>Fernvale Building and Pest inspections – Business Card</title>
<link href="https://fonts.googleapis.com/css2?family=Arimo:wght@400;700&display=swap" rel="stylesheet">
<style>
  :root {
    --backdrop: #d9d9d6;
    --card-white: #ffffff;
    --leaf-green: #8cc63f;
    --leaf-green-light: #a6d65a;
    --leaf-green-dark: #79b330;
    --ink: #1c1c1c;
    --logo-ink: #333333;
    --glass-light: #c9d3d8;
    --glass-dark: #6f8089;
  }
  * { margin: 0; padding: 0; box-sizing: border-box; }
  html, body {
    width: 1200px;
    height: 900px;
    overflow: hidden;
    background: var(--backdrop);
    font-family: "Arimo", Arial, sans-serif;
  }
  .canvas {
    position: relative;
    width: 1200px;
    height: 900px;
  }
  .business-card {
    position: absolute;
    left: 180px;
    top: 210px;
    width: 840px;
    height: 480px;
    background: var(--card-white);
    overflow: hidden;
    box-shadow: 0 14px 30px rgba(0,0,0,0.25);
  }
  .card-header {
    position: absolute;
    left: 0; top: 0;
    width: 100%;
    height: 190px;
    background: var(--card-white);
  }
  .brand {
    position: absolute;
    left: 46px;
    top: 48px;
    display: flex;
    align-items: center;
    gap: 18px;
  }
  .brand-square {
    width: 22px;
    height: 22px;
    background: var(--leaf-green);
    flex: none;
  }
  .brand-name {
    font-size: 38px;
    font-weight: 400;
    line-height: 1.12;
    color: var(--logo-ink);
  }
  .building-visual {
    position: absolute;
    right: 0;
    top: 0;
    width: 300px;
    height: 212px;
    background: linear-gradient(160deg, var(--glass-light) 0%, #9eadb5 45%, var(--glass-dark) 100%);
    clip-path: polygon(38% 0, 100% 0, 100% 100%, 0 100%, 22% 60%);
    z-index: 2;
  }
  .accent-rule {
    position: absolute;
    left: 0;
    top: 190px;
    width: 100%;
    height: 8px;
    background: var(--leaf-green);
  }
  .contact-band {
    position: absolute;
    left: 0;
    top: 204px;
    width: 100%;
    height: 276px;
    background: radial-gradient(ellipse at 45% 45%, var(--leaf-green-light) 0%, var(--leaf-green) 55%, var(--leaf-green-dark) 100%);
    color: var(--ink);
  }
  .section-label {
    position: absolute;
    left: 0;
    width: 760px;
    top: 24px;
    text-align: center;
    font-size: 20px;
    letter-spacing: 0.5px;
  }
  .inspectors {
    position: absolute;
    left: 215px;
    top: 62px;
    display: flex;
    gap: 58px;
  }
  .inspector-name {
    font-size: 30px;
    line-height: 1.1;
  }
  .inspector-phone {
    font-size: 20px;
    letter-spacing: 1px;
    margin-top: 6px;
  }
  .email {
    position: absolute;
    left: 0;
    width: 760px;
    top: 160px;
    text-align: center;
    font-size: 20px;
    letter-spacing: 1px;
  }
  .registration {
    position: absolute;
    left: 100px;
    top: 222px;
    font-size: 20px;
    letter-spacing: 0.4px;
  }
</style>
</head>
<body>
<main class="canvas">
  <article class="business-card">
    <header class="card-header">
      <div class="brand">
        <span class="brand-square"></span>
        <h1 class="brand-name">Fernvale Building<br>and Pest inspections</h1>
      </div>
    </header>
    <div class="building-visual" role="img" aria-label="Glass office tower rising toward the sky"></div>
    <div class="accent-rule"></div>
    <section class="contact-band">
      <p class="section-label">INSPECTORS</p>
      <div class="inspectors">
        <div class="inspector">
          <p class="inspector-name">Dean Harker</p>
          <p class="inspector-phone">0451 278 914</p>
        </div>
        <div class="inspector">
          <p class="inspector-name">Greg Sutcliffe</p>
          <p class="inspector-phone">0419 562 843</p>
        </div>
      </div>
      <p class="email">fernvalebpi@mailpost.example</p>
      <p class="registration">REGISTERED BUILDING PRACTITONER DB-U 58147</p>
    </section>
  </article>
</main>
</body>
</html>
```